Restaurant A5 Catering Brochure/Catalog

We are a fast casual Lebanese restaurant that needs a new multi page Catering brochure made up.

The brochure will be A5 and approx 16 pages.

We will upload media that we would like to use in the brochure in the next 24 hours.

We have uploaded the brochure brief in word file - (Brochurebrief.docx)

We have also uploaded an example of a brochure from another restaurant. it doesn't have to be similar, it just give you an idea. (brochureexample.pdf)

We have also uploaded our stylesheet. (Qamar Kitchen Style Guide.pdf)

and our logo (logo.zip)

The winner will also be able to build a similar brochure plus a function brochure for our other restaurant for additional payment.

We have uploaded many pics. In some cases multiple pictures for the same page. Feel free to choose which pic or pics to use.
Updates

ALL PHOTOS HAVE NOW BEEN UPLOADED. Some pages have multiple photos. Feel free to use any pic or pics you like. Added Wednesday, October 12, 2016

Target Market(s)

We have two target markets that we hope are looking for a different kind of catering. We offer food that is fresh, delicious, and different then traditional catering dishes like pasta or pizza.

The two markets we're after are....
1. Private catering for people looking to cater events at home like birthdays, BBQ's, etc.

2. Schools, Government Offices and Corporate Catering.

Industry/Entity Type

Restaurant

Colors
ec1f27
5c5c5c
c9c9c9
cadf82

Requirements
Must have
• Clean and visual design.
• I would prefer the design was in portrait layout like a book.

```html
<!DOCTYPE html>
<html lang="en">
<head>
<meta charset="utf-8">
<title>Catering – Party Platters</title>
<link href="https://fonts.googleapis.com/css2?family=Lobster&family=Arimo:wght@400;700&display=swap" rel="stylesheet">
<style>
  :root{
    --stage:#3f3f3f;
    --crimson:#a8103a;
    --crimson-deep:#8f0b31;
    --crimson-soft:#c0486f;
    --pill:#ffffff;
    --badge:#f1d3dd;
    --badge-text:#b0204a;
    --ink-light:#ffffff;
    --dip-tones:linear-gradient(135deg,#8a5a3a 0%,#d96a2a 30%,#e8e2d0 60%,#efe6cf 100%);
    --starter-tones:linear-gradient(160deg,#7a4a2a 0%,#d9a85a 40%,#8a5a38 75%,#b07a48 100%);
  }
  *{box-sizing:border-box;margin:0;padding:0}
  html,body{width:1200px;height:1200px;overflow:hidden;background:var(--stage)}
  body{font-family:"Arimo",Arial,sans-serif;position:relative}
  .spread{position:absolute;left:50px;top:211px;width:1100px;height:778px;display:flex;box-shadow:0 20px 50px rgba(0,0,0,.45)}
  .page{position:relative;width:550px;height:778px;overflow:hidden;color:var(--ink-light)}
  .page svg.bg{position:absolute;inset:0}
  .photo{position:absolute;inset:0}
  .photo--dips{background:var(--dip-tones);clip-path:path("M0 0 H230 C285 200 300 520 270 778 H0 Z")}
  .photo--starters{background:var(--starter-tones);clip-path:path("M300 0 H550 V690 C470 690 380 520 335 320 C312 210 302 100 300 0 Z")}
  .pill{position:absolute;background:var(--pill);color:var(--crimson);font-family:"Lobster",cursive;font-size:32px;display:flex;align-items:center;padding-left:34px;height:52px}
  .pill--left{left:270px;top:28px;right:-20px;border-radius:26px 0 0 26px}
  .pill--right{left:-20px;top:62px;width:300px;border-radius:0 26px 26px 0;padding-left:46px}
  .subhead{position:absolute;left:330px;top:100px;font-family:"Lobster",cursive;font-size:24px;font-weight:400}
  .copy{position:absolute;font-size:13.5px;line-height:1.35}
  .copy p{margin-bottom:12px}
  .copy--dips{left:330px;top:140px;width:190px}
  .copy--starters{left:50px;top:140px;width:240px}
  .sizes-label{position:absolute;left:318px;top:560px;width:226px;font-size:12px;white-space:nowrap}
  .badge{position:absolute;border-radius:50%;background:var(--badge);color:var(--badge-text);display:flex;flex-direction:column;align-items:center;justify-content:center;text-align:center;line-height:1.1}
  .badge .size{font-size:13px;font-weight:700}
  .badge .serves{font-size:12px}
  .badge .amount{font-size:26px;font-weight:700}
  .badge--regular{left:322px;top:596px;width:100px;height:100px}
  .badge--large{left:438px;top:580px;width:100px;height:100px}
  .badge--price{left:150px;top:430px;width:124px;height:124px}
  .badge--price .label{font-size:28px}
  .badge--price .amount{font-size:30px;font-weight:400}
  .footnote{position:absolute;bottom:18px;font-size:9px;letter-spacing:.3px;text-transform:uppercase;opacity:.85}
  .footnote--left{left:318px;width:220px}
  .footnote--right{right:20px;bottom:40px}
</style>
</head>
<body>
<main class="spread">
  <section class="page page--dips">
    <svg class="bg" width="550" height="778" viewBox="0 0 550 778">
      <defs>
        <linearGradient id="bandLeft" x1="0" y1="0" x2="1" y2="0">
          <stop offset="0.4" stop-color="#a8103a"/>
          <stop offset="1" stop-color="#c0486f"/>
        </linearGradient>
      </defs>
      <rect width="550" height="778" fill="url(#bandLeft)"/>
    </svg>
    <div class="photo photo--dips" role="img" aria-label="Dip platter with hummus, garlic yogurt, spicy salsa, carrot and celery sticks and pita chips"></div>
    <div class="pill pill--left">Party Platers</div>
    <h2 class="subhead">Dip Platers</h2>
    <div class="copy copy--dips">
      <p>Our fresh dip platters are perfect for any party where good food is welcome.</p>
      <p>Each platter has Hummus, Eggplant, Garlicky Yogurt and Cucumber, Spicy Salsa, and Capsicum and Walnut Dip and your choice of crispy herb pita bread or sliced carrots and celery.</p>
      <p>Make your next event memorable with our delicious homemade dip platters.</p>
    </div>
    <p class="sizes-label">CHOOSE FROM 2 DIFFERENT SIZES:</p>
    <div class="badge badge--regular"><span class="size">REGULAR</span><span class="serves">15 People</span><span class="amount">$25</span></div>
    <div class="badge badge--large"><span class="size">LARGE</span><span class="serves">30 People</span><span class="amount">$50</span></div>
    <p class="footnote footnote--left">*All platters serve 10 people unless otherwise stated</p>
  </section>

  <section class="page page--starters">
    <svg class="bg" width="550" height="778" viewBox="0 0 550 778">
      <defs>
        <linearGradient id="bandRight" x1="0" y1="0" x2="1" y2="0">
          <stop offset="0" stop-color="#8f0b31"/>
          <stop offset="0.5" stop-color="#a8103a"/>
        </linearGradient>
      </defs>
      <rect width="550" height="778" fill="url(#bandRight)"/>
    </svg>
    <div class="photo photo--starters" role="img" aria-label="Starter platter of falafel, cheese rolls, kibbie and pastries with parsley and pickles"></div>
    <div class="pill pill--right">Starters Platter</div>
    <div class="copy copy--starters">
      <p>Our starters platters are sure to make any event even more memorable. Great for Christmas parties, birthdays, office meetings, casual get-togethers, family BBQs, or any other occasion.</p>
      <p>10 Falafel with Mixed Pickles and Tahini Sauce, 10 Sambousek Pastries, 10 Kibbie, 10 Stuffed Vine Leave Rolls, 10 Signature Stuffed Pastries (Choose either Spicy Sausage, Garlicky Chicken, or 3 Cheeses)</p>
    </div>
    <div class="badge badge--price"><span class="label">Price</span><span class="amount">$50</span></div>
    <p class="footnote footnote--right">*All platters serve 10 people unless otherwise stated</p>
  </section>
</main>
</body>
</html>
```